依頼詳細
【サイトマップ】
TOPページ
---HOME
---COMPANY (会社概要/会社沿革)
---BUSINESS (事業内容)
---RECRUIT  (採用情報)
---CONTACT  (問い合わせ)
---NEWS  (新着情報)
【サイト作成においてのポイント】
・レスポンシブデザインでお願いいたします。
・各所の素材は全てURLをお送り下さい。

【イメージ全体配置構図(いれていただきたい要素)】

ワイヤーフレームをご確認ください。
①~⑧までワイヤーフレーム内にふった番号順に詳細を記載しております。

※ワイヤーフレームはあくまでも入れたい要素を並べた一例になります。
各配置、表示位置は変えていただいても問題ございません。
------------------------

①グローバルナビ
配置は上部でお願いいたします。位置は中央を希望いたします。
------

②メインビジュアル
メインビジュアルは動画(アニメーション)挿入の仕様想定で作成して頂きたいです。
参考サイト:http://www.kelvora-sample.com/
http://updates.pimaru-breeze.jp/

1ページまるごと動画(アニメーション)仕様でも問題ございません。
参考サイト:http://www.tosquivel.com/

(こちらでは素材を用意しておりません。確認後、購入手続きをさせていただきますのでURLをお送りください)
サイズはどのデバイスでも横幅が100%になるように考えております。
縦幅はお任せしますので、素材にあわせていただけますと幸いです。
------

③新着情報
新着情報は3つ以上いれていただけますと幸いです
いれていただきたい要素は
・更新日時(年,月,日)
・更新内容のテキスト部分 20文字前後

各テキストの配置箇所、文字色、フォント、文字やボタンのサイズ、幅感等の指定はございません。
ワイヤーフレームにはいれていただきたい要素だけならべています。
------

④事業紹介箇所
入れていただきたい要素は以下になります。
・事業紹介イメージ素材
メイン動画がヘッダー部分のみに表示の場合
背景画像として、サイズは横が100%になるように考えております。
メイン動画が全体の場合
イメージ素材が浮き上がってくるようなアニメーション仕様で考えておりますので、その仕様にあったサイズ、表示方法にしていただけますと幸いです。

極力どのデバイスサイズでもバランスよく見えるような素材をご使用いただけますと幸いです。

・事業内容の名前
(Internet media、Promotion、Influencer Marketing)
・以下テキスト
(KanoMireaはインターネットを軸とした事業を展開しております。)
・下層ページへのリンクボタン

------

⑤入れていただきたい要素は以下になります。
・背景素材
メイン動画がヘッダー部分のみに表示の場合
メイン動画が全体の場合

・遷移先の中に含まれる内容の紹介
(Staff Interview、One Day、Blog)
・以下テキスト
(KanoMireaの福利厚生や、メンバーの1日の勤務スケジュールを公開)
・下層ページへのリンクボタン

------

⑥入れていただきたい要素は以下になります。
・背景素材
メイン動画がヘッダー部分のみに表示の場合
メイン動画が全体の場合

・遷移先の中に含まれる内容の紹介
(overview/ history、Greeting)
・以下テキスト
(会社概要・沿革・代表挨拶)
・下層ページへのリンクボタン

------

⑦フッター
サイト案内
------

⑧会社情報、ロゴ

以上になります。

ご不明点等がございましたらお気軽にお問い合わせ下さい。
何卒よろしくお願い申し上げます。
ページ数
1ページ
希望イメージ
• +5 0 +5
• シンプル
複雑
• 単色
カラフル
• 暗い
明るい
• 日常
高級
• 遊び心
厳粛
• 未来的
伝統的
• 女性的
男性的
希望する色
青系、水色系、グレー系、紫系
納品ファイル
• フォトショップ形式 (.psd)
補足説明
SD又は、FireworksPNGデータ
動画に関しましてはデータ添付またはURLをお送りいただけますと幸いです。
依頼公開後の追記内容
もう少し様々な作品を拝見させていただきたく、延長させていただきました。
引き続き、何卒よろしくお願いいたします。
■ 選んだ理由

全体の雰囲気が1番理想とするものに近く、構図も綺麗なバランスで組み立てられていました。
コーポレートサイトとしてシンプルかつおしゃれ見やすいものに仕上がると思い、rusofu様の作品を選ばせていただきました。

■ 提案者全員のお礼・コメント

各ランサー様
この度は弊社へのコンペへご参加いただき、誠にありがとうございました。
どの作品も大変素晴らしく、当選させていただきたいアイディア、デザインがたくさんありました。
また機会がございましたら、作品をご投稿下さいますと幸いに存じます。
誠にありがとうございました。

```html
<!DOCTYPE html>
<html lang="ja">
<head>
<meta charset="utf-8">
<title>KanoMirea</title>
<link href="https://fonts.googleapis.com/css2?family=Barlow+Condensed:wght@500;600;700&family=Noto+Sans+JP:wght@400;500;700&display=swap" rel="stylesheet">
<style>
:root{
  --navy:#0b1733;
  --navy-2:#142a55;
  --ink:#1b2233;
  --text:#333a48;
  --muted:#8a93a3;
  --blue:#3f86e0;
  --pale:#e6f1fb;
  --line:#d6dbe3;
  --red:#d8333a;
  --white:#ffffff;
}
*{box-sizing:border-box;margin:0;padding:0}
html,body{width:1200px;height:5140px;overflow:hidden}
body{position:relative;background:var(--white);font-family:"Noto Sans JP",sans-serif;color:var(--text)}
.abs{position:absolute}
.display{font-family:"Barlow Condensed",sans-serif;font-weight:700;letter-spacing:.04em;color:var(--ink)}

/* hero */
.hero{left:0;top:0;width:1200px;height:610px;clip-path:polygon(0 0,100% 0,100% 100%,0 92%);
  background:radial-gradient(ellipse at 50% 35%,#2a4f8a 0%,#142a55 40%,#0b1733 80%)}
.brand{display:flex;align-items:center;gap:12px;color:var(--white);font-weight:700;font-size:22px}
.brand .dot{width:34px;height:34px;border-radius:50%;background:var(--white)}
.hero-brand{left:520px;top:26px}
.gnav{left:0;top:92px;width:1200px;display:flex;justify-content:center;gap:44px;
  font-family:"Barlow Condensed",sans-serif;font-weight:600;font-size:15px;letter-spacing:.08em;color:var(--white)}
.hero-title{left:0;top:248px;width:1200px;text-align:center;color:var(--white);font-size:72px;line-height:80px;letter-spacing:.06em}
.hero-sub{left:0;top:410px;width:1200px;text-align:center;color:#cfd8ea;font-size:22px;letter-spacing:.3em}
.pager{left:1022px;top:182px;display:flex;flex-direction:column;gap:12px}
.pager i{display:block;width:7px;height:7px;border-radius:50%;background:#9fb1d3}
.pager i:first-child{background:var(--white)}
.scroll{left:592px;top:480px;width:16px;height:26px;border:2px solid #9fb1d3;border-radius:8px}

.sec-title{font-size:48px;line-height:52px}
.sec-sub{font-size:13px;font-weight:700;color:var(--ink);letter-spacing:.1em}
.body-copy{font-size:13px;line-height:24px;color:var(--text)}
.btn{display:inline-block;width:132px;height:34px;border-radius:17px;background:var(--blue);color:var(--white);
  font-family:"Barlow Condensed",sans-serif;font-weight:600;font-size:13px;letter-spacing:.1em;text-align:center;line-height:34px}

/* business */
.business .sec-title{left:170px;top:820px}
.business .sec-sub{left:172px;top:876px}
.business .body-copy{left:172px;top:960px;width:440px}
.business .btn{left:172px;top:1055px}
.biz-visual{left:680px;top:790px;width:320px;height:300px;border-radius:6px;background:linear-gradient(160deg,#f5f8fc,#dfe7f1)}

/* company */
.company-photo{left:180px;top:1400px;width:460px;height:420px;background:linear-gradient(135deg,#3b3f47 0%,#1d2128 55%,#6b5a45 100%)}
.badge-circle{width:128px;height:128px;border-radius:50%;background:var(--navy);color:var(--white);
  display:flex;flex-direction:column;align-items:center;justify-content:center;
  font-family:"Barlow Condensed",sans-serif;font-weight:700;font-size:17px;line-height:19px;text-align:center}
.badge-circle::after{content:"";width:10px;height:10px;border-right:2px solid #fff;border-bottom:2px solid #fff;transform:rotate(45deg);margin-top:6px}
.company .badge-circle{left:560px;top:1700px}
.company .sec-title{left:700px;top:1520px}
.company .sec-sub{left:702px;top:1580px}
.company .btn{left:758px;top:1656px}

/* recruit */
.pale-band{left:0;top:1950px;width:1200px;height:2180px;background:var(--pale);clip-path:polygon(0 3%,100% 0,100% 97%,0 100%)}
.recruit .sec-title{left:170px;top:2108px}
.recruit .sec-sub{left:172px;top:2164px}
.recruit .body-copy{left:172px;top:2244px;width:460px}
.recruit .btn{left:172px;top:2310px}
.recruit-art{left:690px;top:2060px;width:300px;height:250px;border-radius:6px;background:linear-gradient(160deg,#f7fbff,#d5e5f5)}
.recruit .badge-circle{left:870px;top:2230px;width:116px;height:116px}

/* interview */
.dark-band{left:0;top:2400px;width:1200px;height:540px;background:linear-gradient(180deg,#0f1f44,#0b1733);
  clip-path:polygon(0 14%,100% 0,100% 84%,0 100%)}
.interview-title{left:0;top:2596px;width:1200px;text-align:center;color:var(--white);font-size:30px}
.interview-sub{left:0;top:2636px;width:1200px;text-align:center;color:#c6d2e8;font-size:12px}
.staff{top:2668px;width:180px;height:180px;border-radius:50%;border:4px solid var(--white);background:linear-gradient(180deg,#d9d4cc,#9c9486)}
.interview .btn{left:534px;top:2872px}

/* gallery */
.gallery-title{left:0;top:2976px;width:1200px;text-align:center;font-size:30px}
.gallery-photo{left:168px;top:3040px;width:864px;height:500px;background:linear-gradient(110deg,#7a4a25 0%,#a86a38 45%,#c9c8c6 70%,#8f969f 100%)}
.arrow{top:3280px;width:14px;height:14px;border-left:3px solid var(--ink);border-bottom:3px solid var(--ink)}

/* blog */
.blog-title{left:0;top:3604px;width:1200px;text-align:center;font-size:30px}
.card{top:3680px;width:262px;height:262px;background:var(--white);box-shadow:0 2px 8px rgba(20,40,80,.08)}
.card .thumb{position:absolute;left:16px;top:16px;width:230px;height:120px}
.card .tag{position:absolute;left:16px;top:152px;font-family:"Barlow Condensed",sans-serif;font-weight:700;font-size:15px;color:var(--red);letter-spacing:.06em}
.card .date{position:absolute;left:16px;top:172px;font-size:11px;color:var(--muted)}
.card .txt{position:absolute;left:16px;top:196px;width:230px;font-size:12px;line-height:20px}
.blog .btn{left:534px;top:3975px}

/* news */
.news .sec-title{left:168px;top:4196px}
.news .sec-sub{left:170px;top:4252px}
.news-list{left:500px;top:4150px;width:660px;list-style:none}
.news-list li{display:flex;gap:28px;height:34px;line-height:34px;font-size:12px;border-bottom:1px solid var(--line)}
.news-list time{color:var(--muted);width:86px}

/* contact */
.contact .sec-title{left:168px;top:4414px}
.contact .sec-sub{left:170px;top:4470px}
.form{left:500px;top:4424px;width:420px}
.field{margin-bottom:26px}
.label{font-size:13px;font-weight:700;color:var(--ink);margin-bottom:8px;display:flex;align-items:center;gap:8px}
.req{background:var(--red);color:var(--white);font-size:10px;padding:1px 6px;font-weight:500}
.input{height:32px;border:1px solid var(--line);background:var(--white);width:320px}
.select{width:320px;height:32px;border:1px solid var(--line);font-size:11px;color:var(--muted);line-height:30px;padding-left:10px;position:relative}
.select::after{content:"";position:absolute;right:12px;top:10px;width:6px;height:6px;border-right:1px solid var(--muted);border-bottom:1px solid var(--muted);transform:rotate(45deg)}
.textarea{width:380px;height:190px;border:1px solid var(--line)}

/* footer */
.footer{left:0;top:4880px;width:1200px;height:260px;background:var(--navy);color:#d8deea}
.footer .brand{position:absolute;left:170px;top:40px;font-size:20px}
.footer .brand .dot{width:28px;height:28px}
.footer address{position:absolute;left:170px;top:90px;font-style:normal;font-size:11px;line-height:19px}
.fnav{position:absolute;top:40px;list-style:none;font-size:12px;line-height:22px}
.fnav li{padding-left:12px;position:relative}
.fnav li::before{content:"";position:absolute;left:0;top:9px;width:4px;height:4px;background:var(--blue)}
.fnav small{display:block;font-size:10px;color:#8e9ab3;line-height:14px;margin-bottom:6px}
.copyright{position:absolute;left:0;bottom:22px;width:1200px;text-align:center;font-size:10px;color:#8e9ab3;letter-spacing:.1em}
</style>
</head>
<body>

<header class="abs hero" role="img" aria-label="夜空のような紺色の背景に光のネットワークが広がるメインビジュアル"></header>
<div class="abs brand hero-brand"><span class="dot"></span>KanoMirea</div>
<nav class="abs gnav"><span>OUR BUSINESS</span><span>COMPANY</span><span>RECRUIT</span><span>NEWS</span><span>CONTACT US</span></nav>
<h1 class="abs display hero-title" style="color:#fff">CONNECT WITH<br>ALL OVER THE WORLD.</h1>
<p class="abs hero-sub">世界の人と繋がる事業を</p>
<div class="abs pager"><i></i><i></i><i></i><i></i></div>
<div class="abs scroll"></div>

<section class="business">
  <h2 class="abs display sec-title">OUR BUSINESS</h2>
  <p class="abs sec-sub">事業内容</p>
  <p class="abs body-copy">KanoMireaはインターネットを軸とした事業を展開しております。<br>ここに事業の紹介文が入ります。ここに事業の説明が入ります。<br>一番よいサービスを皆様へお届けしています。</p>
  <a class="abs btn">READ MORE</a>
  <div class="abs biz-visual" role="img" aria-label="インターネットを中心にインフルエンサーマーケティング、プロモーション、インターネットメディアの三事業を示す線画イラスト"></div>
</section>

<section class="company">
  <div class="abs company-photo" role="img" aria-label="ロゴ看板のあるオフィスの壁の写真"></div>
  <div class="abs badge-circle">OFFICE<br>GALLERY</div>
  <h2 class="abs display sec-title">COMPANY</h2>
  <p class="abs sec-sub">会社概要 / 沿革 / 代表挨拶</p>
  <a class="abs btn">READ MORE</a>
</section>

<div class="abs pale-band"></div>

<section class="recruit">
  <h2 class="abs display sec-title">RECRUIT</h2>
  <p class="abs sec-sub">採用情報</p>
  <p class="abs body-copy">KanoMireaの福利厚生や、メンバーの1日の勤務スケジュールを公開。<br>一緒に働く仲間を募集しております。お気軽にご連絡ください。</p>
  <a class="abs btn">READ MORE</a>
  <div class="abs recruit-art" role="img" aria-label="ノートパソコンと虫眼鏡で人材を探す線画イラスト"></div>
  <div class="abs badge-circle">CONTACT<br>US</div>
</section>

<section class="interview">
  <div class="abs dark-band"></div>
  <h2 class="abs display interview-title" style="color:#fff">DAYLY SCHEDULE &amp; STAFF INTERVIEW</h2>
  <p class="abs interview-sub">スタッフの1日のスケジュールとスタッフインタビューをご紹介</p>
  <div class="abs staff" style="left:290px" role="img" aria-label="スタッフの写真"></div>
  <div class="abs staff" style="left:510px" role="img" aria-label="スタッフの写真"></div>
  <div class="abs staff" style="left:730px" role="img" aria-label="スタッフの写真"></div>
  <a class="abs btn">READ MORE</a>
</section>

<section class="gallery">
  <h2 class="abs display gallery-title">OFFICE GALLERY</h2>
  <div class="abs gallery-photo" role="img" aria-label="木目の壁と受付のあるオフィスエントランスの写真"></div>
  <span class="abs arrow" style="left:146px;transform:rotate(45deg)"></span>
  <span class="abs arrow" style="left:1040px;transform:rotate(-135deg)"></span>
</section>

<section class="blog">
  <h2 class="abs display blog-title">STAFF BLOG</h2>
  <article class="abs card" style="left:180px">
    <div class="thumb" style="background:#eef0f3;display:flex;align-items:center;justify-content:center;gap:8px;font-size:14px;font-weight:700;color:#9aa3b1"><span style="width:16px;height:16px;border-radius:50%;background:#c3cad5"></span>KanoMirea</div>
    <p class="tag">PRESS RELEASE</p><p class="date">2018.7.1</p>
    <p class="txt">ダミーです。今日サイトリニューアル</p>
  </article>
  <article class="abs card" style="left:480px">
    <div class="thumb" style="background:linear-gradient(135deg,#c6262b,#e9836b)" role="img" aria-label="赤い小物の写真"></div>
    <p class="tag">UPDATE</p><p class="date">2018.7.1</p>
    <p class="txt">ここに記事のテキストが入ります。順次更新しております。</p>
  </article>
  <article class="abs card" style="left:772px">
    <div class="thumb" style="background:linear-gradient(135deg,#d9cdbf,#8f8a86)" role="img" aria-label="ノートパソコンを操作する手元の写真"></div>
    <p class="tag">UPDATE</p><p class="date">2018.7.1</p>
    <p class="txt">年末年始休業のお知らせ</p>
  </article>
  <a class="abs btn">READ MORE</a>
</section>

<section class="news">
  <h2 class="abs display sec-title">NEWS</h2>
  <p class="abs sec-sub">お知らせ</p>
  <ul class="abs news-list">
    <li><time>2018.7.11</time>WEBサイトをリニューアルしました。ここに新着情報が入ります。</li>
    <li><time>2018.6.11</time>WEBサイトをリニューアルしました。ここに新着情報が入ります。</li>
    <li><time>2018.5.11</time>年末年始休業のお知らせです。</li>
    <li><time>2018.4.11</time>WEBサイトをリニューアルしました。ここに新着情報が入ります。</li>
  </ul>
</section>

<section class="contact">
  <h2 class="abs display sec-title">CONTACT US</h2>
  <p class="abs sec-sub">お問い合わせ</p>
  <form class="abs form">
    <div class="field"><p class="label">お名前 <span class="req">必須</span></p><div class="input"></div></div>
    <div class="field"><p class="label">お問い合わせの種類 <span class="req">必須</span></p><div class="select">選択してください</div></div>
    <div class="field"><p class="label">お問い合わせ内容 <span class="req">必須</span></p><div class="textarea"></div></div>
  </form>
</section>

<footer class="abs footer">
  <div class="brand"><span class="dot"></span>KanoMirea</div>
  <address>株式会社KanoMirea（カノミレア）<br>〒105-0001<br>東京都港区サンプル町1-2-3 ミレアビル5F</address>
  <ul class="fnav" style="left:560px"><li>事業内容</li><small>BUSINESS</small><li>会社概要</li><small>COMPANY</small></ul>
  <ul class="fnav" style="left:760px"><li>採用情報について</li><small>RECRUIT</small><li>スタッフ1日 / インタビュー</li><li>スタッフブログ</li></ul>
  <ul class="fnav" style="left:960px"><li>お知らせ</li><small>NEWS</small><li>お問い合わせ</li><small>CONTACT</small></ul>
  <p class="copyright">© KANO MIREA</p>
</footer>

</body>
</html>
```